VelnoraTek Bright IT Consultancy
All Stationary + ESignaure + Powerpoint Template
Simple
Tomás Barrena Ollé
President & CEO
3er Cjon Calle Fresal 57
Las Brisas, Coyoacán
México DF, 07215
See additional comments
tomas.barrena@velnoratek.mx
www.velnoratek.com.mx
I dont have a permanent local phone number yet, so I dont want to give an informal impression about the company, so Designers I need your creativite to avoid that impression something as simple as "cell&phone" but with all your experience and creativity, an special cell+phone logo for example. Other request is a clean, simple, modern, corporate and professional material.
Go Bright...Go Sky
Go Sky...& Connect
Share...& Succed
Logo Velno
Logo Velno 2
Logo 3
Logo 4
This is an example of standard bullets and numbers in a powerpoint presentation

```html
<!DOCTYPE html>
<html lang="en">
<head>
<meta charset="utf-8">
<title>VelnoraTek – Business Card Back Options</title>
<link rel="stylesheet" href="https://fonts.googleapis.com/css2?family=PT+Sans:ital,wght@0,400;1,400&display=swap">
<style>
  :root {
    --page-bg: #d6d7d8;
    --sheet-bg: #e4e5e6;
    --sheet-border: #a9aaab;
    --label-ink: #3a3a3a;
    --teal: #4d8aa0;
    --teal-deep: #3f7990;
    --white-card: #ffffff;
    --olive: #8e9562;
    --olive-deep: #7f8655;
    --silver: #c6c7c8;
    --silver-deep: #b5b6b8;
    --charcoal: #5a5a5c;
    --charcoal-deep: #4b4b4d;
    --brand-blue: #3f7892;
    --brand-olive: #8c9158;
    --ink-dark: #2f2f30;
    --ink-light: #f2f3f1;
    --ink-pale: #c9d9df;
  }
  * { box-sizing: border-box; margin: 0; padding: 0; }
  html, body {
    width: 1200px; height: 1094px; overflow: hidden;
    background: var(--page-bg);
    font-family: "PT Sans", "Helvetica Neue", Arial, sans-serif;
  }
  .sheet {
    position: absolute; left: 12px; top: 12px; width: 1176px; height: 1070px;
    background: var(--sheet-bg);
    border: 2px solid var(--sheet-border);
  }
  .option { position: absolute; }
  .card {
    position: relative; width: 450px; height: 270px; overflow: hidden;
    box-shadow: 0 6px 14px rgba(0,0,0,0.28);
  }
  .card .tagline {
    position: absolute; font-style: italic; font-size: 29px; line-height: 1;
  }
  .tagline .first { position: absolute; left: 30px; top: 92px; white-space: nowrap; }
  .tagline .second { position: absolute; left: 100px; top: 132px; white-space: nowrap; }
  .brand {
    position: absolute; right: 26px; top: 112px;
    display: flex; align-items: center; gap: 10px;
    font-size: 30px; font-weight: 400; white-space: nowrap;
  }
  .brand .dot { width: 22px; height: 22px; border-radius: 50%; }
  .label {
    margin-top: 22px; text-align: center;
    font-variant: small-caps; letter-spacing: 3px;
    font-size: 20px; color: var(--label-ink);
  }

  .opt-a { left: 360px; top: 22px; }
  .opt-b { left: 118px; top: 392px; }
  .opt-c { left: 609px; top: 392px; }
  .opt-d { left: 118px; top: 726px; }
  .opt-e { left: 609px; top: 726px; }

  .card-a { background: radial-gradient(circle at 60% 40%, var(--teal), var(--teal-deep)); }
  .card-a .first { color: var(--ink-pale); }
  .card-a .second { color: var(--ink-light); }
  .card-a .brand { color: var(--ink-light); }
  .card-a .dot { background: var(--brand-olive); }

  .card-b { background: radial-gradient(circle at 40% 40%, var(--white-card), #eeeeee); }
  .card-b .first { color: var(--brand-blue); }
  .card-b .second { color: var(--brand-olive); }
  .card-b .brand { color: var(--brand-blue); }
  .card-b .dot { background: var(--brand-olive); }

  .card-c { background: radial-gradient(circle at 60% 40%, var(--olive), var(--olive-deep)); }
  .card-c .first { color: #b9bd98; }
  .card-c .second { color: #c3c6a6; }
  .card-c .brand { color: #d6d8c2; }
  .card-c .dot { background: #a9ad85; }

  .card-d { background: radial-gradient(circle at 50% 40%, var(--silver), var(--silver-deep)); }
  .card-d .first { color: var(--ink-dark); }
  .card-d .second { color: var(--ink-light); }
  .card-d .brand { color: var(--brand-blue); }
  .card-d .dot { background: var(--brand-olive); }

  .card-e { background: radial-gradient(circle at 50% 40%, var(--charcoal), var(--charcoal-deep)); }
  .card-e .first { color: var(--ink-light); }
  .card-e .second { color: #b8b9bb; }
  .card-e .brand { color: var(--ink-light); }
  .card-e .dot { background: var(--brand-olive); }
</style>
</head>
<body>
<main class="sheet">
  <section class="option opt-a">
    <div class="card card-a">
      <p class="tagline"><span class="first">Go Bright...</span><span class="second">Go Sky...</span></p>
      <div class="brand"><span class="dot"></span>VelnoraTek</div>
    </div>
    <p class="label">Back Option A</p>
  </section>

  <section class="option opt-b">
    <div class="card card-b">
      <p class="tagline"><span class="first">Go Bright...</span><span class="second">Go Sky...</span></p>
      <div class="brand"><span class="dot"></span>VelnoraTek</div>
    </div>
    <p class="label">Back Option B</p>
  </section>

  <section class="option opt-c">
    <div class="card card-c">
      <p class="tagline"><span class="first">Go Bright...</span><span class="second">Go Sky...</span></p>
      <div class="brand"><span class="dot"></span>VelnoraTek</div>
    </div>
    <p class="label">Back Option C</p>
  </section>

  <section class="option opt-d">
    <div class="card card-d">
      <p class="tagline"><span class="first">Go Bright...</span><span class="second">Go Sky...</span></p>
      <div class="brand"><span class="dot"></span>VelnoraTek</div>
    </div>
    <p class="label">Back Option D</p>
  </section>

  <section class="option opt-e">
    <div class="card card-e">
      <p class="tagline"><span class="first">Go Bright...</span><span class="second">Go Sky...</span></p>
      <div class="brand"><span class="dot"></span>VelnoraTek</div>
    </div>
    <p class="label">Back Option E</p>
  </section>
</main>
</body>
</html>
```